Spirits Bottle Label for American Agave Spirit produced in Maryland

Need to revamp my spirits bottle label to a new innovative design. Looking for a minimalist design that would catch your eye on in a liquor store bottle. I open to designs. Looking for something a lot different than what I currently have wow me with your creativity.

Design Brief:

Logo Name: "Tides" with the "H" positioned horizontally (emphasize the unique horizontal "H").
Color Scheme: Pink or Burgundy and gold (use these as primary colors). With gold being a accent color.
Motto: Include the phrase "Celebrate life with old and new friends" in a subtle, elegant font. Want to keep the 1947 but not as prominent as it is now.
Overall Feel: The design should convey warmth, celebration, and connection, blending a modern touch with timeless appeal.

I also attached a copy of my other brand bottle design thatI love. Barrel & Reed is the name

Target Market(s)

21-65 Year old spirits drinkers, A label that is different than most spirits bottles. Want to catch the eyes of consumers

Industry/Entity Type

spirits industy

Colors

Designer to choose colors to be used in the design.

Requirements
Must have
• Motto, vibrant colors, minimist design
Should not have
• Need to look professional and not be so cluttered

```html
<!DOCTYPE html>
<html lang="en">
<head>
<meta charset="utf-8">
<title>Tides — Spirit Label</title>
<link rel="stylesheet" href="https://fonts.googleapis.com/css2?family=Cinzel:wght@400;600&display=swap">
<style>
  :root {
    --backdrop: #f2f1ef;
    --label-top: #ffffff;
    --label-bottom: #e4e3e2;
    --burgundy: #b7333b;
    --gold: #8a5a22;
    --agave-light: #eee3d3;
    --agave-dark: #b48a57;
  }
  * { margin: 0; padding: 0; box-sizing: border-box; }
  html, body {
    width: 1200px;
    height: 1200px;
    overflow: hidden;
    background: var(--backdrop);
  }
  .canvas {
    position: relative;
    width: 1200px;
    height: 1200px;
  }
  .label {
    position: absolute;
    left: 254px;
    top: 100px;
    width: 692px;
    height: 1000px;
    background: linear-gradient(180deg, var(--label-top) 0%, var(--label-top) 55%, var(--label-bottom) 100%);
    box-shadow: 0 2px 10px rgba(0,0,0,0.08);
  }
  .label__year {
    position: absolute;
    top: 44px;
    left: 0;
    width: 100%;
    text-align: center;
    font-family: "Cinzel", serif;
    font-weight: 400;
    font-size: 44px;
    color: #3a2a1c;
    letter-spacing: 1px;
  }
  .label__agave {
    position: absolute;
    left: 144px;
    top: 142px;
    width: 437px;
    height: 365px;
  }
  .label__brand {
    position: absolute;
    top: 500px;
    left: 0;
    width: 100%;
    text-align: center;
    font-family: "Cinzel", serif;
    font-weight: 600;
    font-size: 150px;
    line-height: 180px;
    color: var(--burgundy);
    letter-spacing: 4px;
  }
  .label__motto {
    position: absolute;
    top: 690px;
    left: 0;
    width: 100%;
    text-align: center;
    font-family: "Cinzel", serif;
    font-weight: 400;
    font-size: 21.5px;
    color: var(--gold);
    letter-spacing: 0.5px;
  }
</style>
</head>
<body>
  <main class="canvas">
    <section class="label">
      <p class="label__year">1947</p>
      <svg class="label__agave" viewBox="0 0 437 365" role="img" aria-label="Engraved illustration of an agave plant in gold line work">
        <defs>
          <radialGradient id="agaveTone" cx="50%" cy="65%" r="60%">
            <stop offset="0%" stop-color="var(--agave-dark)" stop-opacity="0.55"/>
            <stop offset="100%" stop-color="var(--agave-light)" stop-opacity="0.6"/>
          </radialGradient>
        </defs>
        <ellipse cx="218" cy="200" rx="210" ry="165" fill="url(#agaveTone)"/>
      </svg>
      <h1 class="label__brand">Tides</h1>
      <p class="label__motto">Celebrate life with old and new friends</p>
    </section>
  </main>
</body>
</html>
```